Business card for medical clinic

I need an upmarket, modern medical/health business card for my clinic

Contact Information for Business Card

name, address, email, qr code

```html
<!DOCTYPE html>
<html lang="en">
<head>
<meta charset="utf-8">
<title>Corvia Health Partners – Business Card</title>
<link rel="stylesheet" href="https://fonts.googleapis.com/css2?family=Montserrat:wght@400;500;700&display=swap">
<style>
  :root {
    --backdrop: #ecebe8;
    --navy: #1d4a72;
    --sky: #2491c6;
    --accent: #1f9ad8;
    --ink: #2b2b2b;
    --paper: #ffffff;
    --brand-ink: #24507a;
  }
  * { box-sizing: border-box; margin: 0; padding: 0; }
  html, body { width: 1200px; height: 1023px; overflow: hidden; }
  body {
    background: var(--backdrop);
    font-family: "Montserrat", Arial, sans-serif;
    position: relative;
  }
  .card {
    position: absolute;
    width: 600px;
    height: 343px;
    border-radius: 3px;
    box-shadow: 0 10px 24px rgba(0,0,0,0.22);
    overflow: hidden;
  }
  .card-front {
    left: 110px; top: 110px;
    background: linear-gradient(100deg, var(--navy) 0%, #236294 50%, var(--sky) 100%);
    display: flex; align-items: center; justify-content: center;
  }
  .brand {
    display: flex; align-items: center; gap: 12px;
    font-weight: 500; letter-spacing: 0.08em; text-transform: uppercase;
    white-space: nowrap;
  }
  .brand-dot { width: 16px; height: 16px; border-radius: 50%; flex: none; }
  .card-front .brand { color: var(--paper); font-size: 30px; }
  .card-front .brand-dot { background: var(--paper); }

  .card-back {
    left: 490px; top: 480px;
    background: var(--paper);
  }
  .card-back .brand {
    position: absolute; left: 34px; top: 204px;
    color: var(--brand-ink); font-size: 14px; letter-spacing: 0.06em;
  }
  .card-back .brand-dot { background: var(--brand-ink); width: 10px; height: 10px; }
  .divider {
    position: absolute; left: 330px; top: 62px;
    width: 2px; height: 152px; background: var(--accent);
  }
  .contact {
    position: absolute; left: 352px; top: 58px;
    color: var(--ink);
  }
  .person-name { color: var(--accent); font-weight: 700; font-size: 21px; line-height: 1.1; }
  .person-role { font-size: 11px; margin-top: 3px; margin-bottom: 14px; }
  .contact-list { list-style: none; font-size: 11.5px; line-height: 1.6; }
  .contact-list li { display: flex; align-items: center; gap: 8px; }
  .contact-list svg { width: 10px; height: 10px; fill: var(--accent); flex: none; }
  .address { margin-top: 8px; font-size: 11.5px; line-height: 1.45; }
</style>
</head>
<body>
  <section class="card card-front">
    <div class="brand"><span class="brand-dot"></span>Corvia Health Partners</div>
  </section>

  <section class="card card-back">
    <div class="brand"><span class="brand-dot"></span>Corvia Health Partners</div>
    <div class="divider"></div>
    <div class="contact">
      <p class="person-name">Marlen Ashcroft</p>
      <p class="person-role">CEO &amp; Founder</p>
      <ul class="contact-list">
        <li><svg viewBox="0 0 10 10"><path d="M2 0.5 L3.6 0.5 L4.2 2.8 L3 3.7 Q4 6 6.3 7 L7.2 5.8 L9.5 6.4 L9.5 8 Q9.5 9.5 8 9.5 Q1 9 0.5 2 Q0.5 0.5 2 0.5 Z"/></svg>215-555-0142</li>
        <li><svg viewBox="0 0 10 10"><path d="M0.5 2 L9.5 2 L9.5 8 L0.5 8 Z M1 2.5 L5 5.5 L9 2.5" fill="none" stroke="#1f9ad8" stroke-width="1.1"/></svg>info@lumencaregroup.com</li>
        <li><svg viewBox="0 0 10 10"><circle cx="5" cy="5" r="4.5"/><path d="M0.5 5 H9.5 M5 0.5 Q2.5 5 5 9.5 M5 0.5 Q7.5 5 5 9.5" stroke="#fff" stroke-width="0.7" fill="none"/></svg>www.lumencaregroup.com</li>
      </ul>
      <p class="address">88 Meridian Way, Suite 210<br>Lansdale, PA 19446</p>
    </div>
  </section>
</body>
</html>
```